A UK based Lettings and Property Management Company - Maple Crest Property

Maple Crest Property rents and manages properties on behalf of owners in Liverpool, UK. We are looking for a clean, fresh modern design which incororates our logo.

In terms of pages we initially require:

Home
Lettings
Property Management
Landlords
Tenants
About
Contact

In would like to use colours compatible with the logo

Target Market(s)

People looking to rent property
Owners looking to use our services to let their property

Industry/Entity Type

Property

Contact Information for Business Card

Logo prominent on one side
Address to be edited by us as we are moving premises in October
Name Gavin Holloway
Tel number 0151 486 2037
e-mail gavin@maplecrestproperty.co.uk

Font styles to use
Sans Serif

Colors

Designer to choose colors to be used in the design.

Requirements
Must have
• Clean lines
• Fresh
• Easy navigation
• Easy editing
• Data capture

```html
<!DOCTYPE html>
<html lang="en">
<head>
<meta charset="utf-8">
<title>Maple Crest Property – Home</title>
<link href="https://fonts.googleapis.com/css2?family=Lora:wght@400;700&family=Open+Sans:wght@400;600;700&display=swap" rel="stylesheet">
<style>
:root{
  --navy:#0d1340;
  --navy-soft:rgba(34,48,110,.78);
  --ink:#2b2b2b;
  --text:#666;
  --line:#e3e3e3;
  --white:#fff;
  --black:#000;
  --panel:#f6f6f6;
}
*{margin:0;padding:0;box-sizing:border-box}
html,body{width:1200px;height:2381px;overflow:hidden}
body{position:relative;background:var(--white);font-family:'Open Sans',sans-serif;color:var(--text)}
.serif{font-family:'Lora',serif}

/* hero */
.hero{position:absolute;left:0;top:0;width:1200px;height:535px}
.hero-photo{position:absolute;inset:0;background:linear-gradient(180deg,#9fc3e6 0%,#c9dbea 30%,#8a7a62 52%,#5f7d3c 75%,#8c8c86 100%)}
.site-header{position:absolute;left:0;top:0;width:1200px;height:103px;background:var(--navy-soft);display:flex;align-items:center}
.brand{position:absolute;left:106px;top:30px;display:flex;align-items:center;gap:12px;color:var(--white);font-family:'Open Sans',sans-serif;font-weight:700;font-size:26px;letter-spacing:1px;line-height:1}
.brand .mark{width:34px;height:34px;background:var(--white)}
.main-nav{position:absolute;top:48px;left:0;font-family:'Lora',serif;font-weight:700;font-size:13px;color:var(--white)}
.main-nav a{position:absolute;white-space:nowrap;color:inherit;text-decoration:none}

.feature-card{position:absolute;left:100px;top:214px;width:302px;height:249px;background:var(--white);padding:30px 21px 0}
.feature-tag{position:absolute;left:0;top:-12px;height:22px;padding:0 22px 0 14px;background:var(--navy);color:var(--white);font-family:'Lora',serif;font-weight:700;font-size:11px;line-height:22px;clip-path:polygon(0 0,88% 0,100% 50%,88% 100%,0 100%)}
.feature-card h2{font-family:'Lora',serif;font-size:18px;color:var(--navy);font-weight:700}
.specs{display:flex;gap:16px;margin-top:16px;font-family:'Lora',serif;font-size:13px;color:var(--ink)}
.spec-icons{display:flex;align-items:center;margin-top:10px;gap:0}
.spec-icons svg{fill:var(--navy)}
.spec-icons .area{font-family:'Lora',serif;font-size:13px;color:var(--ink);margin-left:6px}
.feature-card .sale{margin-top:26px;font-family:'Lora',serif;font-size:13px;color:var(--ink)}
.feature-card .price{font-family:'Lora',serif;font-weight:700;font-size:26px;color:var(--navy);margin-top:6px}

/* about */
.about-photo{position:absolute;left:98px;top:595px;width:475px;height:287px;border:4px solid var(--white);box-shadow:0 0 0 1px var(--line);background:linear-gradient(135deg,#e8e2b0 0%,#a6b36a 40%,#5d7a45 70%,#6e7a82 100%)}
.about-text{position:absolute;left:617px;top:590px;width:490px}
.about-text h2{font-family:'Lora',serif;font-weight:700;font-size:30px;color:var(--navy);line-height:1.3}
.about-text p{font-size:13px;line-height:23px;margin-top:18px}
.btn{display:inline-block;margin-top:24px;height:31px;padding:0 24px;line-height:31px;border-radius:16px;background:var(--navy);color:var(--white);font-family:'Lora',serif;font-weight:700;font-size:12px}

/* values band */
.values{position:absolute;left:0;top:940px;width:1200px;height:182px;background:linear-gradient(90deg,#2d3462 0%,#4a527a 45%,#5a5f82 70%,#3a4068 100%)}
.values::after{content:"";position:absolute;inset:0;background:rgba(30,38,90,.45)}
.value{position:absolute;top:52px;z-index:1;display:flex;gap:0;color:var(--white)}
.value svg{fill:var(--white);position:absolute;left:0;top:10px}
.value h3{font-family:'Lora',serif;font-weight:700;font-size:21px;margin-left:97px}
.value p{font-size:13px;line-height:23px;margin:2px 0 0 97px;width:230px}

/* deals */
.deals{position:absolute;left:98px;top:1178px;width:1002px;height:757px;border:1px solid var(--line)}
.deals h2{position:absolute;top:34px;width:100%;text-align:center;font-family:'Lora',serif;font-weight:700;font-size:31px;color:#444}
.deals .intro{position:absolute;top:92px;left:150px;width:700px;text-align:center;font-size:12.5px;line-height:24px}
.listing{position:absolute;width:450px;height:252px;border:1px solid var(--line)}
.listing h4{position:absolute;left:21px;top:14px;font-size:14px;font-weight:600;color:#444}
.listing .photo{position:absolute;left:21px;top:54px;width:186px;height:136px}
.listing .info{position:absolute;left:219px;top:54px;width:210px}
.listing .rate{background:var(--panel);padding:4px 8px 6px;color:var(--ink);font-size:15px;font-weight:600;line-height:24px}
.listing .rate span{display:block;font-size:13px}
.listing .info p{font-size:12.5px;line-height:24px;margin:8px 0 0 8px}
.listing .info a{display:block;margin:2px 0 0 8px;font-size:12.5px;color:var(--navy);text-decoration:underline}
.listing .features{position:absolute;left:0;bottom:0;width:100%;height:35px;display:flex;border-top:1px solid var(--line)}
.listing .features span{width:102px;border-right:1px solid var(--line);font-size:12.5px;text-align:center;line-height:34px;color:#666}
.listing .features span:first-child{width:100px}
.listing .features span:last-child{flex:1;border-right:0}

/* footer */
.site-footer{position:absolute;left:0;top:2000px;width:1200px;height:381px;background:var(--black);color:var(--white)}
.footer-brand{position:absolute;left:0;top:62px;width:100%;display:flex;justify-content:center;align-items:center;gap:14px;font-family:'Open Sans',sans-serif;font-weight:700;font-size:32px;letter-spacing:1px}
.footer-brand .mark{width:40px;height:40px;background:var(--white)}
.footer-nav{position:absolute;top:162px;left:0;width:100%;display:flex;justify-content:center;font-family:'Lora',serif;font-weight:700;font-size:13px}
.footer-nav a{color:var(--white);text-decoration:none;padding:0 34px;border-right:1px solid var(--white);line-height:16px}
.footer-nav a:last-child{border-right:0}
.rule{position:absolute;left:98px;width:1004px;height:1px;background:#333}
.contact{position:absolute;left:98px;top:249px;display:flex;align-items:center;gap:10px;font-family:'Lora',serif;font-size:13px}
.contact svg{fill:var(--white)}
.socials{position:absolute;right:98px;top:246px;display:flex;gap:13px}
.socials span{width:22px;height:22px;border-radius:3px}
.copyright{position:absolute;top:333px;width:100%;text-align:center;font-family:'Lora',serif;font-size:13px}
</style>
</head>
<body>

<section class="hero">
  <div class="hero-photo" role="img" aria-label="Photograph of a large two-storey family house with garages and landscaped front garden"></div>
  <header class="site-header">
    <div class="brand"><span class="mark"></span>MAPLE CREST PROPERTY</div>
    <nav class="main-nav">
      <a style="left:502px">Home</a>
      <a style="left:570px">Lettings</a>
      <a style="left:650px">Property Management</a>
      <a style="left:815px">Landlords</a>
      <a style="left:906px">Tenants</a>
      <a style="left:987px">About</a>
      <a style="left:1053px">Contact</a>
    </nav>
  </header>
  <div class="feature-card">
    <div class="feature-tag">Featured</div>
    <h2>Home in UK</h2>
    <div class="specs"><span>Bedrooms 3</span><span>Bathrooms 3</span><span>Area</span></div>
    <div class="spec-icons">
      <svg width="52" height="40" viewBox="0 0 52 40"><rect x="6" y="10" width="40" height="16"/><rect x="2" y="6" width="4" height="28"/><rect x="46" y="6" width="4" height="28"/><rect x="11" y="13" width="12" height="6" fill="#fff"/><rect x="29" y="13" width="12" height="6" fill="#fff"/></svg>
      <svg width="56" height="40" viewBox="0 0 56 40" style="margin-left:36px"><rect x="26" y="2" width="3" height="8"/><path d="M17 18a10 8 0 0 1 21 0z"/><g><circle cx="19" cy="23" r="1.5"/><circle cx="25" cy="23" r="1.5"/><circle cx="31" cy="23" r="1.5"/><circle cx="37" cy="23" r="1.5"/><circle cx="20" cy="29" r="1.5"/><circle cx="27" cy="29" r="1.5"/><circle cx="35" cy="29" r="1.5"/><circle cx="22" cy="35" r="1.5"/><circle cx="32" cy="35" r="1.5"/></g></svg>
      <svg width="40" height="40" viewBox="0 0 40 40" style="margin-left:22px"><rect x="8" y="10" width="22" height="22" fill="none" stroke="#0d1340" stroke-width="3"/><rect x="2" y="2" width="3" height="12"/><rect x="2" y="2" width="12" height="3"/><rect x="34" y="18" width="3" height="18"/></svg>
      <span class="area">4300 Sq Ft</span>
    </div>
    <div class="sale">For Sale</div>
    <div class="price">$540,000</div>
  </div>
</section>

<div class="about-photo" role="img" aria-label="Photograph of a family walking hand in hand outside their home in sunlight"></div>
<section class="about-text">
  <h2>Excepteur sint occaecat proident</h2>
  <p>Lorem ipsum dolor sit amet, consectetur adipiscing elit, sed do eiusmod tempor incididunt ut labore et dolore magna aliqua. Ut enim ad minim veniam, quis nostrud exercitation ullamco laboris nisi ut aliquip ex ea commodo consequat. Duis aute irure dolor in reprehenderit.</p>
  <p>Nam libero tempore, cum soluta nobis est eligendi optio cumque nihil impedit quo minus id quod maxime placeat facere possimus, omnis voluptas assumenda est, omnis dolor</p>
  <span class="btn">Read More &gt;&gt;</span>
</section>

<section class="values" role="img" aria-label="Background photograph of a couple viewing a property, tinted navy">
  <div class="value" style="left:98px">
    <svg width="60" height="58" viewBox="0 0 60 58"><rect x="2" y="24" width="12" height="30" rx="2"/><path d="M18 26 L30 4 q6 -2 6 6 L33 22 H52 q6 2 4 8 L50 50 q-2 4 -6 4 H18z"/></svg>
    <div><h3>Trust</h3><p>Lorem ipsum dolor sit&nbsp; consectetur adipiscing elit, sed do eiusmod tempor</p></div>
  </div>
  <div class="value" style="left:436px">
    <svg width="64" height="56" viewBox="0 0 64 56"><path d="M26 4C12 4 2 12 2 22c0 6 3 10 8 13l-3 9 11-6c2 1 5 1 8 1 14 0 24-8 24-17S40 4 26 4z" fill="none" stroke="#fff" stroke-width="4"/><path d="M54 22c6 3 8 8 8 12 0 5-3 9-7 11l2 8-9-5c-2 1-4 1-6 1-6 0-11-2-14-5" fill="none" stroke="#fff" stroke-width="4"/></svg>
    <div><h3>Customer Support</h3><p>Lorem ipsum dolor sit&nbsp; consectetur adipiscing elit, sed do eiusmod tempor</p></div>
  </div>
  <div class="value" style="left:790px">
    <svg width="52" height="60" viewBox="0 0 52 60"><path d="M4 2h30l14 14v42H4z" fill="none" stroke="#fff" stroke-width="4"/><rect x="13" y="24" width="26" height="3"/><rect x="13" y="33" width="26" height="3"/><rect x="13" y="42" width="26" height="3"/></svg>
    <div><h3>Free Documentation</h3><p>Lorem ipsum dolor sit amet, consectetur adipiscing elit, sed do eiusmod tempor</p></div>
  </div>
</section>

<section class="deals">
  <h2>We are Offering the Best Real Estate Deals</h2>
  <p class="intro">Lorem Ipsum is that it has a more-or-less normal distribution of letters, as opposed to using 'Content here, content here', making it look like readable English. Many desktop publishing packages</p>

  <article class="listing" style="left:37px;top:179px">
    <h4>Doloremque Laudantium</h4>
    <div class="photo" role="img" aria-label="Photograph of a detached suburban house with a green lawn" style="background:linear-gradient(180deg,#a9c8e8 0%,#d9d4c4 45%,#5f9a3c 70%,#4e8a30 100%)"></div>
    <div class="info"><div class="rate">$7,500 Per Month<span>- Single Family Home</span></div><p>Lorem ipsum dolor sit amet, consectetuer adipiscing elit,...</p><a>More Details &gt;&gt;</a></div>
    <div class="features"><span>4 Bedrooms</span><span>3 Bathrooms</span><span>2 Garages</span><span></span></div>
  </article>
  <article class="listing" style="left:519px;top:179px">
    <h4>Doloremque Laudantium</h4>
    <div class="photo" role="img" aria-label="Photograph of a brick family house with flowering trees" style="background:linear-gradient(180deg,#8fb8e6 0%,#c8b8a6 45%,#7a8f4a 70%,#5a9a38 100%)"></div>
    <div class="info"><div class="rate">$7,500 Per Month<span>- Single Family Home</span></div><p>Lorem ipsum dolor sit amet, consectetuer adipiscing elit,...</p><a>More Details &gt;&gt;</a></div>
    <div class="features"><span>4 Bedrooms</span><span>3 Bathrooms</span><span>2 Garages</span><span></span></div>
  </article>
  <article class="listing" style="left:37px;top:466px">
    <h4>Doloremque Laudantium</h4>
    <div class="photo" role="img" aria-label="Photograph of a modern house lit up at dusk" style="background:linear-gradient(180deg,#2c3f9a 0%,#4a5ab0 40%,#c8b890 65%,#5a6a4a 100%)"></div>
    <div class="info"><div class="rate">$7,500 Per Month<span>- Single Family Home</span></div><p>Lorem ipsum dolor sit amet, consectetuer adipiscing elit,...</p><a>More Details &gt;&gt;</a></div>
    <div class="features"><span>4 Bedrooms</span><span>3 Bathrooms</span><span>2 Garages</span><span></span></div>
  </article>
  <article class="listing" style="left:519px;top:466px">
    <h4>Doloremque Laudantium</h4>
    <div class="photo" role="img" aria-label="Photograph of a row of suburban homes along a curving street" style="background:linear-gradient(180deg,#5f92d8 0%,#a9c2e0 35%,#6e8a4e 60%,#8a8a86 100%)"></div>
    <div class="info"><div class="rate">$7,500 Per Month<span>- Single Family Home</span></div><p>Lorem ipsum dolor sit amet, consectetuer adipiscing elit,...</p><a>More Details &gt;&gt;</a></div>
    <div class="features"><span>4 Bedrooms</span><span>3 Bathrooms</span><span>2 Garages</span><span></span></div>
  </article>
</section>

<footer class="site-footer">
  <div class="footer-brand"><span class="mark"></span>MAPLE CREST PROPERTY</div>
  <nav class="footer-nav">
    <a>Home</a><a>Lettings</a><a>Property Management</a><a>Landlords</a><a>Tenants</a><a>About</a><a>Contact</a>
  </nav>
  <div class="rule" style="top:219px"></div>
  <div class="contact">
    <svg width="16" height="16" viewBox="0 0 16 16"><circle cx="8" cy="8" r="7"/><path d="M1 8h14M8 1c3 3 3 11 0 14M8 1c-3 3-3 11 0 14" stroke="#000" stroke-width="1" fill="none"/></svg>
    <span>www.maplecrestproperty.co.uk</span>
    <svg width="14" height="14" viewBox="0 0 14 14" style="margin-left:14px"><path d="M3 1l3 3-2 2c1 2 2 3 4 4l2-2 3 3-2 2C6 13 1 8 1 3z"/></svg>
    <span>0151 486 2037</span>
  </div>
  <div class="socials">
    <span style="background:#3b5aa8"></span><span style="background:#29a3e0"></span><span style="background:#c8401f"></span><span style="background:#e08a1e"></span><span style="background:#1e9ad6"></span>
  </div>
  <div class="rule" style="top:301px"></div>
  <div class="copyright">Copyright © 2017 MaplecrestProperty. All Rights Reserved.</div>
</footer>

</body>
</html>
```